deceased estate cleaning services and cosmetic renovating

house frontage signage design
cur flute sign will be 600mm x 450 mm and no larger
is to be mounted of fence out front of projects as advertizing

Target Market(s)

elderly people and there sibling that need help

Colors
cadf82
85cae6
fbed22
85acd3
ffcf3e

Requirements
Must have
• clear phone number, email and business Name and logo
Should not have
• to much info and NO dark colors

```html
<!DOCTYPE html>
<html lang="en">
<head>
<meta charset="utf-8">
<title>Tidynest – Fence Sign</title>
<link rel="stylesheet" href="https://fonts.googleapis.com/css2?family=Cinzel:wght@700&family=Playfair+Display:ital@1&family=Patrick+Hand+SC&family=Arimo:wght@700&display=swap">
<style>
  :root {
    --paper: #ffffff;
    --ink: #111111;
    --ink-soft: #1d1d1d;
    --sky: #85cae6;
    --leaf: #66c21a;
    --band-start: #4fcf1f;
    --band-end: #a9f232;
    --mark-light: #cadf82;
    --mark-deep: #7fd23a;
  }
  html, body {
    margin: 0;
    padding: 0;
    width: 1200px;
    height: 900px;
    overflow: hidden;
    background: var(--paper);
  }
  .sign {
    position: relative;
    width: 1200px;
    height: 900px;
    background: var(--paper);
    font-family: "Arimo", Arial, sans-serif;
    font-weight: 700;
    color: var(--ink);
  }
  .sign__intro {
    position: absolute;
    left: 40px;
    top: 30px;
    margin: 0;
    font-family: "Playfair Display", Georgia, serif;
    font-style: italic;
    font-weight: 400;
    font-size: 36px;
    line-height: 1;
    color: var(--ink-soft);
  }
  .sign__headline {
    position: absolute;
    left: 38px;
    top: 80px;
    margin: 0;
    font-family: "Patrick Hand SC", "Comic Sans MS", cursive;
    font-weight: 400;
    font-size: 56px;
    line-height: 1;
    letter-spacing: 1px;
    color: var(--sky);
  }
  .brand-mark {
    position: absolute;
    left: 500px;
    top: 85px;
    width: 230px;
    height: 230px;
    border-radius: 50%;
    background: radial-gradient(circle at 40% 35%, var(--mark-light), var(--mark-deep));
  }
  .brand-name {
    position: absolute;
    left: 0;
    width: 1200px;
    top: 348px;
    margin: 0;
    text-align: center;
    padding-left: 10px;
    box-sizing: border-box;
    font-family: "Cinzel", "Times New Roman", serif;
    font-weight: 700;
    font-size: 84px;
    letter-spacing: 6px;
    line-height: 1.1;
    color: var(--ink);
  }
  .values {
    position: absolute;
    left: 0;
    width: 1200px;
    top: 436px;
    margin: 0;
    text-align: center;
    padding-left: 10px;
    box-sizing: border-box;
    font-size: 32px;
    font-weight: 700;
    line-height: 1.2;
    color: var(--leaf);
  }
  .values span::before {
    content: "•";
    font-size: 20px;
    margin: 0 6px 0 10px;
    vertical-align: 4px;
  }
  .services {
    position: absolute;
    left: 0;
    width: 1200px;
    top: 535px;
    margin: 0;
    padding: 0 0 0 10px;
    box-sizing: border-box;
    list-style: none;
    text-align: center;
    font-size: 36px;
    font-weight: 700;
    line-height: 57px;
    color: var(--ink-soft);
  }
  .phone {
    position: absolute;
    left: 0;
    width: 1200px;
    top: 666px;
    margin: 0;
    text-align: center;
    padding-left: 10px;
    box-sizing: border-box;
    font-size: 90px;
    font-weight: 700;
    line-height: 1;
    letter-spacing: -1px;
    color: var(--ink);
  }
  .cleanup-scene {
    position: absolute;
    left: 905px;
    top: 658px;
    width: 275px;
    height: 150px;
    border-radius: 8px;
    background: linear-gradient(135deg, #c6584a 0%, #f3e7c4 50%, #9fb7b0 100%);
  }
  .contact-band {
    position: absolute;
    left: 0;
    top: 825px;
    width: 1200px;
    height: 75px;
    background: linear-gradient(90deg, var(--band-start), var(--band-end));
    font-size: 40px;
    font-weight: 700;
    line-height: 75px;
    color: var(--ink);
  }
  .contact-band__email,
  .contact-band__web {
    position: absolute;
    top: 0;
    transform: translateX(-50%);
    white-space: nowrap;
  }
  .contact-band__email { left: 342px; }
  .contact-band__web { left: 859px; }
</style>
</head>
<body>
  <main class="sign">
    <p class="sign__intro">We’re here to help</p>
    <h2 class="sign__headline">DECLUTTER YOUR LIFE</h2>

    <div class="brand-mark" aria-hidden="true"></div>
    <h1 class="brand-name">TIDYNEST</h1>
    <p class="values"><span>Quality</span><span>Pride</span><span>Professionalism</span></p>

    <ul class="services">
      <li>Deceased Estate Cleanups</li>
      <li>House Maintenance &amp; Cosmetic Repairs</li>
    </ul>

    <p class="phone">0400 555 218</p>

    <div class="cleanup-scene" role="img" aria-label="Illustration of a removal truck collecting household clutter from a house"></div>

    <footer class="contact-band">
      <span class="contact-band__email">info@tidynest.com.au</span>
      <span class="contact-band__web">www.tidynest.com.au</span>
    </footer>
  </main>
</body>
</html>
```